Weather card for guests at Fenwick’s Beach House

I am looking to have a card designed for my guests who stay over. The card should show the weather for the next day (emoji's), quote of the day, Activities of the day. It's for a beach house so it should be coastal/Beachy themed. The weather should have a high and a low. (I will fill in each card). It should be front and back. It should be a fun project. Think modern farmhouse. The top of each card should say something like Another great Day at 7 Harbor
Updates

If you google "turn down Service letter" or "hotel weather card". It will provide examples

Target Market(s)

Our guests who visit our beach house

Font styles to use
Sans Serif

Colors
0054AA
0677BA
7BADD7
CADEEF
E8F1F8

Requirements
Must have
• weather options, quote of the day, activity for the day
Nice to have
• Sand, seashells, seagulls
Should not have
• Should not be too busy and not childish

```html
<!DOCTYPE html>
<html lang="en">
<head>
<meta charset="utf-8">
<title>7 Harbor – Guest Weather Card</title>
<link rel="stylesheet" href="https://fonts.googleapis.com/css2?family=Quicksand:wght@500&family=Mulish:wght@600;700&display=swap">
<style>
  :root {
    --navy: #0054AA;
    --ocean: #0677BA;
    --sky: #7BADD7;
    --mist: #CADEEF;
    --foam: #E8F1F8;
    --white: #FFFFFF;
    --table: #ECECEC;
  }
  * { box-sizing: border-box; margin: 0; padding: 0; }
  html, body { width: 1200px; height: 993px; overflow: hidden; }
  body {
    background: var(--table);
    font-family: "Mulish", sans-serif;
    position: relative;
  }
  .card {
    position: absolute;
    width: 518px;
    height: 827px;
    overflow: hidden;
    box-shadow: 2px 3px 6px rgba(0,0,0,0.18);
  }
  .card--front { left: 51px; top: 62px; }
  .card--back { left: 631px; top: 103px; }

  .beach-photo {
    position: absolute; inset: 0;
    background: linear-gradient(180deg,
      #8fb3dc 0%, #a9c6e6 12%, #7fa9d6 24%, #b9cfe4 30%,
      #5d7d96 33%, #a6c3cf 36%, #8a8068 40%,
      #c9b89c 44%, #d3c4a8 60%, #c8b799 80%, #b8a688 100%);
  }

  .heading {
    position: absolute; left: 0; right: 0; top: 24px;
    text-align: center; color: var(--navy);
  }
  .heading__lead {
    font-family: "Mulish", sans-serif; font-weight: 700;
    font-size: 29px; line-height: 1; letter-spacing: -0.2px;
  }
  .heading__place {
    font-family: "Quicksand", sans-serif; font-weight: 500;
    font-size: 86px; line-height: 1;
    letter-spacing: -1px;
  }

  .section-title {
    position: absolute; left: 0; right: 0;
    text-align: center; color: var(--navy);
    font-weight: 700; font-size: 19px; line-height: 1;
  }
  .section-title--weather { top: 175px; }
  .section-title--temps { top: 333px; }

  .weather-options {
    position: absolute; left: 29px; top: 209px;
    display: flex; gap: 20px;
  }
  .weather-tile {
    position: relative; width: 76px; height: 86px; padding-top: 10px;
  }
  .weather-tile__face {
    width: 76px; height: 76px; border-radius: 7px;
    background: var(--sky);
    display: flex; align-items: center; justify-content: center;
  }
  .weather-tile__pin {
    position: absolute; left: 29px; top: 0;
    width: 18px; height: 18px; border-radius: 50%;
    background: var(--white); border: 2px solid var(--sky);
  }
  .weather-tile svg { width: 58px; height: 58px; }
  .weather-tile svg * { fill: none; stroke: var(--white); stroke-width: 1.6; stroke-linecap: round; stroke-linejoin: round; }

  .temperatures {
    position: absolute; left: 29px; top: 363px;
    display: flex; gap: 21px;
  }
  .temp-field {
    width: 219px; height: 37px; border-radius: 8px;
    background: var(--foam); border: 2px solid var(--sky);
    color: var(--sky); font-weight: 700; font-size: 13px;
    padding-left: 11px; display: flex; align-items: center;
  }

  .note-box {
    position: absolute; left: 30px; width: 457px; height: 297px;
    background: var(--foam); border: 2px solid var(--sky); border-radius: 8px;
    text-align: center; color: var(--navy);
    font-weight: 700; font-size: 19px; padding-top: 9px;
  }
  .note-box--quote { top: 189px; }
  .note-box--activities { top: 500px; }
</style>
</head>
<body>

<section class="card card--front">
  <div class="beach-photo" role="img" aria-label="Photo of a spiral seashell resting on sand, with sea, hills and blue sky blurred behind"></div>
  <header class="heading">
    <p class="heading__lead">Another great day at</p>
    <p class="heading__place">7 Harbor</p>
  </header>

  <h2 class="section-title section-title--weather">Tomorrow’s Weather</h2>
  <div class="weather-options">
    <div class="weather-tile"><span class="weather-tile__pin"></span><div class="weather-tile__face">
      <svg viewBox="0 0 56 56" aria-label="Sunny"><circle cx="28" cy="28" r="11"/><path d="M28 5v8M28 43v8M5 28h8M43 28h8M11.7 11.7l5.7 5.7M38.6 38.6l5.7 5.7M11.7 44.3l5.7-5.7M38.6 17.4l5.7-5.7"/></svg>
    </div></div>
    <div class="weather-tile"><span class="weather-tile__pin"></span><div class="weather-tile__face">
      <svg viewBox="0 0 56 56" aria-label="Partly cloudy"><path d="M14 26a6 6 0 0 1 11-3M17 14v3M8 22h3M10 16l2 2M22 16l-2 2M10 30l2-2"/><path d="M14 40h32a6 6 0 0 0 0-12 9 9 0 0 0-17-2 7 7 0 0 0-15 3 5.5 5.5 0 0 0 0 11z"/></svg>
    </div></div>
    <div class="weather-tile"><span class="weather-tile__pin"></span><div class="weather-tile__face">
      <svg viewBox="0 0 56 56" aria-label="Cloudy"><path d="M12 38h32a6 6 0 0 0 0-12 10 10 0 0 0-19-2 7 7 0 0 0-13 3 5.5 5.5 0 0 0 0 11z"/></svg>
    </div></div>
    <div class="weather-tile"><span class="weather-tile__pin"></span><div class="weather-tile__face">
      <svg viewBox="0 0 56 56" aria-label="Rain"><path d="M12 32h32a6 6 0 0 0 0-12 10 10 0 0 0-19-2 7 7 0 0 0-13 3 5.5 5.5 0 0 0 0 11z"/><path d="M15 39l-2 4a2 2 0 0 0 4 0zM28 39l-2 4a2 2 0 0 0 4 0zM41 39l-2 4a2 2 0 0 0 4 0z"/></svg>
    </div></div>
    <div class="weather-tile"><span class="weather-tile__pin"></span><div class="weather-tile__face">
      <svg viewBox="0 0 56 56" aria-label="Snow"><path d="M28 5v46M8 16.5l40 23M8 39.5l40-23M23 8l5 5 5-5M23 48l5-5 5 5M8 22l6-3-2-6M48 34l-6 3 2 6M8 34l6 3-2 6M48 22l-6-3 2-6"/></svg>
    </div></div>
  </div>

  <h2 class="section-title section-title--temps">Temperatures</h2>
  <div class="temperatures">
    <div class="temp-field">High</div>
    <div class="temp-field">Low</div>
  </div>
</section>

<section class="card card--back">
  <div class="beach-photo" role="img" aria-label="Soft-focus beach photo with sand, sea, hills and blue sky"></div>
  <header class="heading">
    <p class="heading__lead">Another great day at</p>
    <p class="heading__place">7 Harbor</p>
  </header>
  <div class="note-box note-box--quote">Quote of the day</div>
  <div class="note-box note-box--activities">Activities for the day</div>
</section>

</body>
</html>
```